RK LAW
Stationary Envelopes and Cards
RK LAW - Law
Creative Brief
Professional
Howard P. Lindqvist
Attorney At Law
347 N. 4th Avenue Las Vegas NV 89104
nvrklaw@mailbrook.net
NVRKLAW.NET

```html
<!DOCTYPE html>
<html lang="en">
<head>
<meta charset="utf-8">
<title>RK LAW – Business Card</title>
<link rel="stylesheet" href="https://fonts.googleapis.com/css2?family=Noto+Serif:ital,wght@0,400;1,400&family=Open+Sans:wght@400&display=swap">
<style>
  :root {
    --page-bg: #3a3a3c;
    --card-white: #ffffff;
    --brand-blue: #1f6fb8;
    --tagline-grey: #6d7277;
    --wave-light: #4fa3e0;
    --wave-dark: #0f5ea8;
    --swoosh-grey: #a9acb0;
    --text-white: #ffffff;
  }
  html, body {
    margin: 0;
    width: 1200px;
    height: 780px;
    overflow: hidden;
    background: var(--page-bg);
  }
  .business-card {
    position: absolute;
    left: 100px;
    top: 104px;
    width: 1000px;
    height: 572px;
    border-radius: 36px;
    overflow: hidden;
    background: var(--card-white);
    box-shadow: 0 12px 30px rgba(0,0,0,0.35);
  }
  .card-shapes {
    position: absolute;
    inset: 0;
  }
  .firm {
    position: absolute;
    left: 70px;
    top: 80px;
  }
  .firm-name {
    font-family: "Noto Serif", serif;
    font-weight: 400;
    font-size: 72px;
    line-height: 1;
    color: var(--brand-blue);
    letter-spacing: 2px;
  }
  .firm-tagline {
    margin-top: 14px;
    font-family: "Noto Serif", serif;
    font-size: 28px;
    letter-spacing: 1px;
    color: var(--tagline-grey);
    text-transform: uppercase;
  }
  .attorney {
    position: absolute;
    right: 532px;
    top: 368px;
    text-align: right;
    font-family: "Noto Serif", serif;
    color: var(--text-white);
  }
  .attorney-name {
    font-style: italic;
    font-size: 27px;
    line-height: 1.2;
  }
  .attorney-title {
    font-style: italic;
    font-size: 23px;
    line-height: 1.3;
  }
  .attorney-address {
    margin-top: 22px;
    font-size: 21px;
    line-height: 1.35;
  }
  .divider {
    position: absolute;
    left: 488px;
    top: 366px;
    width: 2px;
    height: 150px;
    background: rgba(255,255,255,0.8);
  }
  .contact-list {
    position: absolute;
    left: 510px;
    top: 360px;
    margin: 0;
    padding: 0;
    list-style: none;
    font-family: "Open Sans", sans-serif;
    font-size: 21px;
    color: var(--text-white);
  }
  .contact-list li {
    display: flex;
    align-items: center;
    gap: 14px;
    height: 40px;
  }
  .contact-icon {
    width: 22px;
    height: 22px;
    flex: none;
  }
</style>
</head>
<body>
  <div class="business-card">
    <svg class="card-shapes" viewBox="0 0 1000 572" width="1000" height="572" aria-hidden="true">
      <defs>
        <linearGradient id="waveFill" x1="0" y1="0" x2="0.6" y2="1">
          <stop offset="0" stop-color="#4fa3e0"/>
          <stop offset="1" stop-color="#0f5ea8"/>
        </linearGradient>
      </defs>
      <path class="grey-swoosh" fill="#a9acb0"
            d="M330,322 C620,300 860,205 1000,92 L1000,140 C860,240 620,322 330,322 Z"/>
      <path class="blue-wave" fill="url(#waveFill)"
            d="M0,360 C360,372 760,310 1000,150 L1000,572 L0,572 Z"/>
    </svg>

    <div class="firm">
      <div class="firm-name">RK LAW</div>
      <div class="firm-tagline">Counsel you can trust</div>
    </div>

    <div class="attorney">
      <div class="attorney-name">Howard P. Lindqvist</div>
      <div class="attorney-title">Attorney At Law</div>
      <div class="attorney-address">347 N. 4th Avenue<br>Las Vegas NV 89104</div>
    </div>

    <div class="divider"></div>

    <ul class="contact-list">
      <li>
        <svg class="contact-icon" viewBox="0 0 24 24" aria-hidden="true"><path fill="#fff" d="M6.6 10.8a15 15 0 0 0 6.6 6.6l2.2-2.2c.3-.3.7-.4 1-.2 1.1.4 2.3.6 3.6.6.6 0 1 .4 1 1V20c0 .6-.4 1-1 1C10.6 21 3 13.4 3 4c0-.6.4-1 1-1h3.5c.6 0 1 .4 1 1 0 1.3.2 2.5.6 3.6.1.3 0 .7-.2 1z"/></svg>
        <span>(702) 555-0187</span>
      </li>
      <li>
        <svg class="contact-icon" viewBox="0 0 24 24" aria-hidden="true"><rect x="6" y="2" width="12" height="6" fill="#fff"/><rect x="3" y="9" width="18" height="9" rx="1.5" fill="#fff"/><rect x="6" y="15" width="12" height="7" fill="#fff" stroke="#0f5ea8" stroke-width="1"/></svg>
        <span>(702) 555-0192</span>
      </li>
      <li>
        <svg class="contact-icon" viewBox="0 0 24 24" aria-hidden="true"><circle cx="12" cy="12" r="11" fill="#fff"/><text x="12" y="16.5" text-anchor="middle" font-family="Open Sans, sans-serif" font-size="13" fill="#0f5ea8">@</text></svg>
        <span>nvrklaw@mailbrook.net</span>
      </li>
      <li>
        <svg class="contact-icon" viewBox="0 0 24 24" aria-hidden="true"><circle cx="12" cy="12" r="10" fill="none" stroke="#fff" stroke-width="2"/><ellipse cx="12" cy="12" rx="4.5" ry="10" fill="none" stroke="#fff" stroke-width="1.6"/><line x1="2" y1="12" x2="22" y2="12" stroke="#fff" stroke-width="1.6"/></svg>
        <span>www.nvrklaw.net</span>
      </li>
    </ul>
  </div>
</body>
</html>
```